Alternative Health Practice - Website redesign

With regard to the welcome image, stock photos can't show the faces of other people. And please don't submit a design for a one-page website.
Hello, I am redesigning a website and need some help from a professional.
The old website is here: peter-lindqvist.net (pls note I don't want to reuse the welcome photo from the old site). Much of the written content will remain the same, so note that I also need a page layout/text colour etc that works for text heavy pages: ie www.peter-lindqvist.net/somatic-articles and www.peter-lindqvist.net/client-reviews
My effort at redesigning is underway here: https://pjlindqvist.sitebuildr.net/my-site-7
The original sitebuildr template is this one: https://www.sitebuildr.net/website-template/view/html/2868?originUrl=https%3A%2F%2Fwww.sitebuildr.net%2Fwebsite%2Ftemplates%2Fhtml%2Fhealth-wellness&tpClick=view_button&esi=6305f015-f1b5-4bdd-8dfa-47b7d756bb68
I'm pretty happy with the colour palette. My name Peter Johan Lindqvist is now the "brand" without Rooted Stillness subtitle. Regarding the Welcome section, if you are going to use my photos, it probably needs to be those two that are already there. If you want to put a stock photo there instead, that's fine.
If you want to propose something quite different to my design, I'm happy to receive design files in Photoshop or whatever and then subsequently replicate on Sitebuildr. Up to you.
Target Market(s)
Mostly women, some men ages 28-60.
Coding
Coded - Design and coding required
Number of Pages Required
5+ page
Look and feel
Each slider illustrates characteristics of the customer's brand and the style your logo design should communicate.

```html
<!DOCTYPE html>
<html lang="en">
<head>
<meta charset="utf-8">
<title>Peter Lindqvist – The Practice</title>
<link href="https://fonts.googleapis.com/css2?family=Montserrat:wght@400;500;600;700;800&display=swap" rel="stylesheet">
<style>
:root{
  --ink:#2a2a2a;
  --dark:#2d2d2d;
  --darker:#222222;
  --gold:#e3a72a;
  --gold-deep:#c98d14;
  --cream:#f8e2a6;
  --cream-light:#fdf3d8;
  --text:#5b5b5b;
  --white:#ffffff;
}
*{box-sizing:border-box;margin:0;padding:0}
html,body{width:1200px;height:3596px;overflow:hidden}
body{font-family:"Montserrat",Arial,sans-serif;color:var(--text);background:var(--white);position:relative}
.abs{position:absolute}
.btn{display:inline-block;background:var(--gold);color:var(--white);font-size:15px;font-weight:500;padding:14px 28px;border-radius:2px}

/* header + hero */
.hero{left:0;top:0;width:1200px;height:700px;background:linear-gradient(100deg,#2f2a24 0%,#4e4337 38%,#8a7458 62%,#c7a67a 82%,#e9d4ae 100%)}
.hero-photo{position:absolute;left:0;top:0;width:100%;height:100%}
.brand{left:112px;top:32px;display:flex;align-items:center;gap:14px}
.brand-mark{width:46px;height:46px;border-radius:50%;background:var(--gold)}
.brand-name{font-size:22px;font-weight:600;color:var(--white);letter-spacing:2px}
.nav{left:468px;top:50px;display:flex;gap:44px;font-size:15px;font-weight:500;color:var(--white);letter-spacing:.5px}
.nav .active{position:relative}
.nav .active::after{content:"";position:absolute;left:0;right:0;bottom:-12px;height:3px;background:var(--gold)}
.nav .active::before{content:"";position:absolute;left:50%;bottom:-30px;width:8px;height:8px;border-radius:50%;background:var(--white);transform:translateX(-50%)}
.hero-title{left:112px;top:262px;font-size:76px;font-weight:800;color:var(--white);letter-spacing:3px}
.hero-lead{left:112px;top:372px;width:440px;font-size:24px;line-height:1.4;color:var(--white)}
.hero .btn{position:absolute;left:112px;top:492px}
.dots{left:572px;top:652px;display:flex;gap:10px}
.dots span{width:12px;height:12px;border-radius:50%;background:rgba(255,255,255,.5)}
.dots span:first-child{background:var(--white)}

/* about */
.about-title{left:112px;top:800px;font-size:28px;font-weight:700;color:var(--ink);letter-spacing:1px}
.about-sub{left:112px;top:860px;font-size:20px;font-weight:500;color:var(--ink)}
.about-body{left:112px;top:906px;width:480px;font-size:15px;line-height:1.75}
.about-body p+p{margin-top:22px}
.about .btn{position:absolute;left:112px;top:1128px}
.about-photo{left:640px;top:788px;width:392px;height:380px;background:linear-gradient(120deg,#d9b77e 0%,#b98a4c 40%,#6f4b2e 70%,#3e3a35 100%)}

/* energy */
.energy{left:0;top:1200px;width:1200px;height:880px}
.energy-title{left:0;top:1366px;width:1200px;text-align:center;font-size:26px;font-weight:700;color:var(--white);letter-spacing:1px}
.energy-title::after{content:"";display:block;width:240px;height:1px;background:rgba(255,255,255,.6);margin:16px auto 0}
.energy-photo{left:112px;top:1472px;width:488px;height:456px;background:linear-gradient(160deg,#b0aaa2 0%,#8f8982 45%,#d9cfc2 75%,#efe6d9 100%)}
.energy-photo .tag{position:absolute;left:132px;bottom:60px;display:flex;align-items:center;gap:12px}
.energy-photo .tag i{width:40px;height:40px;border-radius:50%;background:var(--gold)}
.energy-photo .tag b{font-size:24px;font-weight:600;color:var(--white);letter-spacing:2px}
.energy-mark{left:872px;top:1388px;width:100px;height:100px;border-radius:50%;background:var(--gold)}
.energy-head{left:636px;top:1494px;font-size:26px;font-weight:500;color:var(--white)}
.energy-body{left:636px;top:1550px;width:460px;font-size:15px;line-height:1.75;color:#d8d8d8}
.energy-body strong{color:var(--white);font-weight:700}
.energy-body p+p{margin-top:22px}
.energy .btn{position:absolute;left:636px;top:1860px}

/* reviews */
.reviews-title{left:0;top:2178px;width:1200px;text-align:center;font-size:26px;font-weight:600;color:var(--ink);letter-spacing:1px}
.reviews-title::after{content:"";display:block;width:340px;height:1px;background:#bbb;margin:18px auto 0}
.card{width:524px;height:290px;background:linear-gradient(90deg,var(--gold) 0%,var(--cream) 45%,var(--cream-light) 100%);display:flex;align-items:center;padding:0 24px}
.avatar{width:190px;height:212px;flex:none}
.card-text{margin-left:28px}
.card-name{font-size:17px;font-weight:600;color:var(--ink);margin-bottom:14px}
.card-quote{font-size:14px;line-height:1.6;color:#444}
.stars{margin-top:10px;display:flex;gap:3px}
.reviews .btn{position:absolute;left:500px;top:2948px}

/* footer */
.footer{left:0;top:3060px;width:1200px;height:536px}
.foot-mark{left:196px;top:3190px;width:70px;height:70px;border-radius:50%;background:var(--gold)}
.foot-name{left:112px;top:3272px;font-size:26px;font-weight:600;color:var(--white);letter-spacing:2px}
.foot-addr{left:112px;top:3320px;font-size:15px;line-height:1.75;color:#ddd}
.foot-addr b{display:block;color:var(--white);font-size:17px;margin-bottom:4px}
.contact{left:608px;top:3210px;width:480px;height:300px;background:var(--white);padding:24px 36px}
.contact h3{text-align:center;font-size:17px;font-weight:600;color:var(--ink);letter-spacing:1px;margin-bottom:18px}
.fields{display:grid;grid-template-columns:1fr 1fr;gap:16px 20px}
.field{height:38px;border:1px solid #ccc;font-size:13px;color:#999;padding:10px 12px}
.contact .btn{margin:22px 0 0 170px;padding:12px 24px;font-size:14px}
.copyright{left:0;top:3554px;width:1200px;height:42px;background:var(--darker);color:#ccc;font-size:13px;text-align:center;line-height:42px;border-top:2px solid var(--gold)}
</style>
</head>
<body>

<section class="abs hero">
  <div class="hero-photo" role="img" aria-label="Photo of a woman smiling with eyes closed in warm sunlight"></div>
  <div class="abs brand"><span class="brand-mark"></span><span class="brand-name">PETER LINDQVIST</span></div>
  <nav class="abs nav"><span class="active">THE PRACTICE</span><span>ABOUT ME</span><span>FEEDBACK</span><span>APPROACH</span><span>CONTACT</span></nav>
  <h1 class="abs hero-title">WELCOME</h1>
  <p class="abs hero-lead">Discover deeper layers of awareness through somatic writing, reflection, and practice</p>
  <span class="btn">Read Articles</span>
  <div class="abs dots"><span></span><span></span></div>
</section>

<section class="about">
  <h2 class="abs about-title">ABOUT PETER LINDQVIST</h2>
  <p class="abs about-sub">Rooted Stillness Teacher</p>
  <div class="abs about-body">
    <p>Growing up in Scotland I had a strong connection with nature and the outdoors. Playing outside with friends, with bikes, ball sports, and later mountaineering and rock climbing, was what most interested me.</p>
    <p>I studied at a Scottish university and worked in London for a number of years as a civil servant. I subsequently set up a property business and in 2006, relocated to Spain.</p>
  </div>
  <span class="btn">Read More</span>
  <div class="abs about-photo" role="img" aria-label="Portrait photo of the practitioner"></div>
</section>

<section class="abs energy">
  <svg width="1200" height="880" viewBox="0 0 1200 880" style="position:absolute;left:0;top:0">
    <path d="M0 40 Q600 -30 1200 40 L1200 840 Q600 900 0 840 Z" fill="var(--dark)"/>
    <path d="M0 32 Q600 -30 1200 32" fill="none" stroke="var(--gold)" stroke-width="8"/>
    <path d="M0 848 Q600 900 1200 848" fill="none" stroke="var(--gold)" stroke-width="8"/>
  </svg>
</section>
<h2 class="abs energy-title">ENERGY HEALING</h2>
<div class="abs energy-photo" role="img" aria-label="Photo of a hands-on healing session">
  <div class="tag"><i></i><b>PETER LINDQVIST</b></div>
</div>
<div class="abs energy-mark"></div>
<h3 class="abs energy-head">The Practice</h3>
<div class="abs energy-body">
  <p><strong>A session typically begins by clarifying your intention or wish.</strong> You may be facing physical or emotional challenges or seeking help with another aspect of your life, such as family or relationship problems.</p>
  <p>Guided by your intention, I will use skills based in touch, movement and perception to facilitate greater congruence between your energy and your physical body. Via this deep listening to the body we will stimulate your natural capacity for healing and growth and you may discover something new about yourself.</p>
</div>
<span class="abs btn" style="left:636px;top:1860px">Book a Session</span>

<section class="reviews">
  <h2 class="abs reviews-title">OUR CUSTOMER REVIEW</h2>

  <div class="abs card" style="left:56px;top:2282px">
    <div class="avatar" role="img" aria-label="Photo of reviewer" style="background:linear-gradient(135deg,#7aa0c2,#c8a68a)"></div>
    <div class="card-text">
      <div class="card-name">Tom Hartley</div>
      <div class="card-quote">I went to see Peter with 3 separate problems. I had very painful sciatica on one occasion and a painful elbow and shoulder on another.</div>
      <div class="stars"><svg width="110" height="20" viewBox="0 0 110 20" fill="var(--gold)"><g id="st"><path d="M10 1l2.6 6 6.4.5-4.9 4.2 1.5 6.3L10 14.6 4.4 18l1.5-6.3L1 7.5 7.4 7z"/></g><use href="#st" x="22"/><use href="#st" x="44"/><use href="#st" x="66"/><use href="#st" x="88"/></svg></div>
    </div>
  </div>

  <div class="abs card" style="left:620px;top:2282px">
    <div class="avatar" role="img" aria-label="Photo of reviewer" style="background:linear-gradient(135deg,#b9a48c,#6f5d4c)"></div>
    <div class="card-text">
      <div class="card-name">Elena Ruiz Navarro</div>
      <div class="card-quote">When I arrived at your practice the first time I was completely blocked, totally despondent. I left feeling recovered and started to feel less passive, more energetic.</div>
      <div class="stars"><svg width="110" height="20" viewBox="0 0 110 20" fill="var(--gold)"><use href="#st"/><use href="#st" x="22"/><use href="#st" x="44"/><use href="#st" x="66"/><use href="#st" x="88"/></svg></div>
    </div>
  </div>

  <div class="abs card" style="left:56px;top:2640px">
    <div class="avatar" role="img" aria-label="Photo of reviewer" style="background:linear-gradient(135deg,#a3b08a,#6b5a40)"></div>
    <div class="card-text">
      <div class="card-name">Lucía Ortega Vidal</div>
      <div class="card-quote">You have given me a lot of confidence in myself. You are showing me a new way of life. And I've learned that it is possible to handle the physical.</div>
      <div class="stars"><svg width="110" height="20" viewBox="0 0 110 20" fill="var(--gold)"><use href="#st"/><use href="#st" x="22"/><use href="#st" x="44"/><use href="#st" x="66"/><use href="#st" x="88"/></svg></div>
    </div>
  </div>

  <div class="abs card" style="left:620px;top:2640px">
    <div class="avatar" role="img" aria-label="Photo of reviewer" style="background:linear-gradient(135deg,#8fb3d6,#c9b49a)"></div>
    <div class="card-text">
      <div class="card-name">Margot Delacroix</div>
      <div class="card-quote">I discovered Rooted Stillness 2 years ago and it amazes me how it has changed my approach to many aspects of my life.</div>
      <div class="stars"><svg width="110" height="20" viewBox="0 0 110 20" fill="var(--gold)"><use href="#st"/><use href="#st" x="22"/><use href="#st" x="44"/><use href="#st" x="66"/><use href="#st" x="88"/></svg></div>
    </div>
  </div>

  <span class="btn">View More Reviews</span>
</section>

<footer class="abs footer">
  <svg width="1200" height="536" viewBox="0 0 1200 536" style="position:absolute;left:0;top:0">
    <path d="M0 60 Q600 -20 1200 60 L1200 536 L0 536 Z" fill="var(--dark)"/>
    <path d="M0 52 Q600 -20 1200 52" fill="none" stroke="var(--gold)" stroke-width="6"/>
  </svg>
</footer>
<div class="abs foot-mark"></div>
<div class="abs foot-name">PETER LINDQVIST</div>
<address class="abs foot-addr" style="font-style:normal">
  <b>ADDRESS</b>
  Rua das Laranjeiras 12b<br>
  Bairro Alto<br>
  Porto, Portugal, 4050-001<br>
  Telephone/WhatsApp: +351 91 000 4471
</address>
<form class="abs contact">
  <h3>CONTACT US</h3>
  <div class="fields">
    <div class="field">Name</div>
    <div class="field">Email</div>
    <div class="field">Telephone</div>
    <div class="field">Message</div>
  </div>
  <span class="btn">Submit</span>
</form>
<div class="abs copyright">© 2025 Peter Johan Lindqvist</div>

</body>
</html>
```